12" Touchscreen Interface Graphic Design

We have a touchscreen control system already designed with rudimentary graphics. The functionality is there, we need to make the graphics look more professional.
The new graphics design is to be 'modular' so that things can be moved within the touchscreen software.
By modular i mean that i need to for example add or remove pumps from the system, change the piping layout, move location of the various graphical elements.
I have enough graphics skills to be able to re-size, stretch, colorize the submitted design to adapt it specifically to the ongoing changing needs of the interface.
I can "cut up" the submitted design to make my individual graphical elements (for example 80x100px image for the pump) that i can then move around where i want for future systems that have different hardware configurations.
Attached are screenshots of how the interface looks at the moment, with some comments on the side.
The graphical elements need ideally to have the same pixel dimensions as on the screenshot. If changes are recommended for a specific reason, each element within the overall display should have dimensions in increments of 10px
Also attached is a screenshot from one of our other unrelated control systems that has a graphics style we would like to be close to.
Look and feel
Each slider illustrates characteristics of the customer's brand and the style your logo design should communicate.

```html
<!DOCTYPE html>
<html lang="en">
<head>
<meta charset="utf-8">
<title>Chiller Plant Control</title>
<link rel="stylesheet" href="https://fonts.googleapis.com/css2?family=Share+Tech&family=Share+Tech+Mono&display=swap">
<style>
:root{
  --bg:#000;
  --cyan:#1ad8e6;
  --yellow:#f5ea1a;
  --panel:#1c1f2a;
  --panel-edge:#5a6070;
  --green:#0a9a12;
  --green-dark:#067a0c;
  --blue-top:#2a3cff;
  --blue-bot:#05106a;
  --text:#ffffff;
  --gray-top:#f2f2f2;
  --gray-mid:#6a6a6a;
  --metal-dark:#3c3c3c;
  --metal-light:#d6d6d6;
}
*{box-sizing:border-box;margin:0;padding:0}
html,body{width:1200px;height:736px;overflow:hidden;background:var(--bg)}
body{font-family:"Share Tech Mono",monospace;color:var(--text)}
.screen{position:absolute;left:0;top:0;width:1280px;height:785px;transform:scale(.9375);transform-origin:0 0}
.piping{position:absolute;left:0;top:0}
.readout{position:absolute;width:100px;height:40px;background:var(--panel);border:1px solid var(--panel-edge);border-radius:6px;display:flex;align-items:center;justify-content:center;font-size:23px}
.btn{position:absolute;background:linear-gradient(var(--blue-top),var(--blue-bot));display:flex;align-items:center;justify-content:center;text-align:center;font-size:13px;line-height:13px;border:1px solid #0a1a8a}
.hours{position:absolute;width:80px;height:19px;background:#000;border:1px solid #fff;font-size:13px;display:flex;align-items:center;justify-content:center}
.pump{position:absolute;width:80px;height:92px;border-radius:4px;background:linear-gradient(90deg,var(--metal-dark),var(--metal-light) 45%,var(--metal-dark))}
.pump-num{position:absolute;left:0;right:0;top:64px;text-align:center;font-size:20px;line-height:20px;color:#fff}
.pump-label{position:absolute;width:160px;text-align:center;font-family:"Share Tech",sans-serif;font-size:22px;line-height:24px}
.system-enable{position:absolute;left:20px;top:365px;width:200px;height:100px;background:linear-gradient(var(--gray-top),var(--gray-mid) 50%,#3a3a3a 52%,#cfcfcf);border:1px solid #999;display:flex;align-items:center;justify-content:center;text-align:center;font-family:"Share Tech",sans-serif;font-size:22px;line-height:24px}
.config{position:absolute;left:240px;top:365px;width:100px;height:100px;background:var(--panel);border:1px solid var(--panel-edge);display:flex;align-items:center;justify-content:center;text-align:center;font-size:13px;line-height:13px}
.chiller{position:absolute;width:160px;height:200px}
.ch-temps{display:flex;height:40px}
.ch-temps div{width:80px;background:var(--panel);border:1px solid var(--panel-edge);display:flex;align-items:center;justify-content:center;font-size:21px}
.ch-row{display:flex;height:18px;font-size:13px}
.ch-row div{width:80px;background:var(--green);border:1px solid #5fd060;display:flex;align-items:center;justify-content:center}
.ch-freeze{height:18px;background:var(--green);border:1px solid #5fd060;font-size:13px;text-align:center;line-height:16px}
.ch-toggle{height:60px;background:linear-gradient(var(--blue-top),var(--blue-bot) 45%,#05105a);display:flex;flex-direction:column;justify-content:space-around;align-items:center;font-size:14px;padding:4px 0}
.ch-name{height:46px;background:linear-gradient(#1ac020,var(--green-dark));border-radius:0 0 30px 30px;display:flex;flex-direction:column;align-items:center;padding-top:6px;font-size:13px;gap:4px}
.ch-name span{border:1px solid #fff;padding:1px 5px;background:var(--green)}
.target{position:absolute;left:220px;top:706px;width:100px;height:79px;background:var(--panel);border:1px solid var(--panel-edge);border-radius:6px;text-align:center}
.target .val{font-size:23px;height:40px;line-height:38px;border-bottom:1px solid var(--panel-edge)}
.target .lbl{font-size:12px;line-height:14px;padding-top:4px}
.mode{position:absolute;left:380px;top:745px;width:440px;height:40px;background:var(--panel);border:1px solid var(--panel-edge);display:flex;align-items:center;justify-content:center;font-size:22px;letter-spacing:3px}
</style>
</head>
<body>
<div class="screen">
<svg class="piping" width="1280" height="785" viewBox="0 0 1280 785">
  <g stroke="var(--cyan)" stroke-width="6" fill="none">
    <path d="M0 75H980V140M460 75V415H980V480M540 75V140M760 75V140M540 415V480M760 415V480"/>
  </g>
  <g fill="var(--cyan)">
    <polygon points="380,75 400,55 400,95"/>
    <polygon points="540,136 520,156 560,156"/><polygon points="760,136 740,156 780,156"/><polygon points="980,136 960,156 1000,156"/>
    <polygon points="540,476 520,496 560,496"/><polygon points="760,476 740,496 780,496"/><polygon points="980,476 960,496 1000,496"/>
  </g>
  <g stroke="var(--yellow)" stroke-width="6" fill="none">
    <path d="M80 195H40V315H80M160 195H200V315H160M160 315H400M380 315V597H400"/>
    <path d="M80 605H40V725H80M160 605H200V725H160M160 725H1200V115H618V135M838 115V135M1058 115V135M1200 455H618V475M838 455V475M1058 455V475"/>
  </g>
  <g fill="var(--yellow)">
    <polygon points="420,315 400,295 400,335"/><polygon points="420,597 400,577 400,617"/><polygon points="400,725 380,705 380,745"/>
    <polygon points="618,155 598,135 638,135"/><polygon points="838,155 818,135 858,135"/><polygon points="1058,155 1038,135 1078,135"/>
    <polygon points="618,495 598,475 638,475"/><polygon points="838,495 818,475 858,475"/><polygon points="1058,495 1038,475 1078,475"/>
  </g>
  <g class="valve">
    <circle cx="1140" cy="115" r="20" fill="var(--green)" stroke="#fff" stroke-width="2"/>
    <path d="M1140 96A19 19 0 0 0 1140 134Z" fill="var(--yellow)"/><polygon points="1120,115 1140,103 1140,127" fill="#b0b000"/>
    <circle cx="1140" cy="455" r="20" fill="var(--green)" stroke="#fff" stroke-width="2"/>
    <path d="M1140 436A19 19 0 0 0 1140 474Z" fill="var(--yellow)"/><polygon points="1120,455 1140,443 1140,467" fill="#b0b000"/>
  </g>
</svg>

<div class="readout" style="left:220px;top:55px">12.1°C</div>
<div class="readout" style="left:220px;top:295px">12.1°C</div>

<div class="btn" style="left:0;top:96px;width:80px;height:60px">RESET<br>HOURS</div>
<div class="hours" style="left:80px;top:96px">12345 HRS</div>
<div class="pump" style="left:80px;top:120px" role="img" aria-label="Sea water pump 1 drawing: motor on top of a flanged pump body"><div class="pump-num">1</div></div>
<div class="pump-label" style="left:40px;top:214px">SEA WATER</div>
<div class="pump" style="left:80px;top:240px" role="img" aria-label="Sea water pump 2 drawing: motor on top of a flanged pump body"><div class="pump-num">2</div></div>
<div class="btn" style="left:0;top:296px;width:80px;height:60px">RESET<br>HOURS</div>
<div class="hours" style="left:80px;top:336px">12345 HRS</div>
<div class="btn" style="left:220px;top:195px;width:120px;height:60px">CHANGE<br>SEA WATER<br>PUMP</div>

<div class="system-enable">SYSTEM ENABLE<br>SWITCH OFF</div>
<div class="config">SHOW<br>SYSTEM<br>CONFIG<br>BUTTONS</div>

<div class="btn" style="left:0;top:505px;width:80px;height:60px">RESET<br>HOURS</div>
<div class="hours" style="left:80px;top:506px">12345 HRS</div>
<div class="pump" style="left:80px;top:530px" role="img" aria-label="Circulation pump 1 drawing: motor on top of a flanged pump body"><div class="pump-num">1</div></div>
<div class="pump-label" style="left:40px;top:624px">CIRCULATION</div>
<div class="pump" style="left:80px;top:650px" role="img" aria-label="Circulation pump 2 drawing: motor on top of a flanged pump body"><div class="pump-num">2</div></div>
<div class="btn" style="left:0;top:705px;width:80px;height:60px">RESET<br>HOURS</div>
<div class="hours" style="left:80px;top:746px">12345 HRS</div>
<div class="btn" style="left:220px;top:605px;width:120px;height:60px">CHANGE<br>CIRCULATION<br>PUMP</div>

<div class="btn" style="left:160px;top:725px;width:60px;height:60px;font-size:18px">-</div>
<div class="target"><div class="val">12.1°C</div><div class="lbl">TARGET<br>12°C</div></div>
<div class="btn" style="left:320px;top:725px;width:60px;height:60px;font-size:18px">+</div>
<div class="mode">SUMMER - COOLING MODE</div>
<div class="btn" style="left:820px;top:725px;width:120px;height:60px">CHANGE TO<br>HEATING MODE</div>

<div class="chiller" style="left:500px;top:155px"><div class="ch-temps"><div>12.1°C</div><div>12.1°C</div></div><div class="ch-row"><div>1 HP!!!</div><div>12.1 BAR</div></div><div class="ch-row"><div>LP!!!</div><div>12.1 BAR</div></div><div class="ch-freeze">FREEZE STOP</div><div class="ch-toggle"><div>ENABLED</div><div>PRESS TO INHIBIT</div></div><div class="ch-name">CHILLER #1<span>12345 HRS</span></div></div>
<div class="chiller" style="left:720px;top:155px"><div class="ch-temps"><div>12.1°C</div><div>12.1°C</div></div><div class="ch-row"><div>1 HP!!!</div><div>12.1 BAR</div></div><div class="ch-row"><div>LP!!!</div><div>12.1 BAR</div></div><div class="ch-freeze">FREEZE STOP</div><div class="ch-toggle"><div>ENABLED</div><div>PRESS TO INHIBIT</div></div><div class="ch-name">CHILLER #2<span>12345 HRS</span></div></div>
<div class="chiller" style="left:940px;top:155px"><div class="ch-temps"><div>12.1°C</div><div>12.1°C</div></div><div class="ch-row"><div>1 HP!!!</div><div>12.1 BAR</div></div><div class="ch-row"><div>LP!!!</div><div>12.1 BAR</div></div><div class="ch-freeze">FREEZE STOP</div><div class="ch-toggle"><div>ENABLED</div><div>PRESS TO INHIBIT</div></div><div class="ch-name">CHILLER #3<span>12345 HRS</span></div></div>
<div class="chiller" style="left:500px;top:495px"><div class="ch-temps"><div>12.1°C</div><div>12.1°C</div></div><div class="ch-row"><div>1 HP!!!</div><div>12.1 BAR</div></div><div class="ch-row"><div>LP!!!</div><div>12.1 BAR</div></div><div class="ch-freeze">FREEZE STOP</div><div class="ch-toggle"><div>ENABLED</div><div>PRESS TO INHIBIT</div></div><div class="ch-name">CHILLER #4<span>12345 HRS</span></div></div>
<div class="chiller" style="left:720px;top:495px"><div class="ch-temps"><div>12.1°C</div><div>12.1°C</div></div><div class="ch-row"><div>1 HP!!!</div><div>12.1 BAR</div></div><div class="ch-row"><div>LP!!!</div><div>12.1 BAR</div></div><div class="ch-freeze">FREEZE STOP</div><div class="ch-toggle"><div>ENABLED</div><div>PRESS TO INHIBIT</div></div><div class="ch-name">CHILLER #5<span>12345 HRS</span></div></div>
<div class="chiller" style="left:940px;top:495px"><div class="ch-temps"><div>12.1°C</div><div>12.1°C</div></div><div class="ch-row"><div>1 HP!!!</div><div>12.1 BAR</div></div><div class="ch-row"><div>LP!!!</div><div>12.1 BAR</div></div><div class="ch-freeze">FREEZE STOP</div><div class="ch-toggle"><div>ENABLED</div><div>PRESS TO INHIBIT</div></div><div class="ch-name">CHILLER #6<span>12345 HRS</span></div></div>
</div>
</body>
</html>
```